Aviation Maintenance & Aircraft Cleaning Website

We need a fairly simple modern sleek website . Our company does aviation maintenance , aircraft cleaning , maintenance tracking . We work on KT420 HELICOPTERS , BELVANKO T82 HELICOPTERS , MORVELL TARRANT 512 HELICOPTERS. We would like a website that can be mobile as well with future ideas that an app where you could book cleanings and maintenance . Right now the biggest thing is for our customer to see a website , be able to book our services online and see our staff . the website must be modern and clean .

Target Market(s)

Aviation maintenance , aviation cleaning ,

Logo Text

TW but 1 image unlike the one i uploaded which is two . Im open for different aviation designs

Number of Pages Required

5+ page

Font styles to use
Serif

Requirements
Must have
• Home page , Aircraft Maintenance , Aircraft Cleaning , About Us , Contact , Careers

TW Aviation is insured and all of our mechanics are licensed by the plain badge with an plain badge & Powerplant rating. ( FRONT PAGE )

Home page should have a simple nice picture of a KT420 or Belvanko T82 . My Logo as you can see seems like two logos . i would like 1 logo and made of the two if possible . (New ideas are welcome . )

Book a Cleaning Calendar should in the aircraft cleaning page . The aircraft cleaning page should have a picture of cleaning a helicopter or private jet .

Aircraft maintenance page should have a mechanic working on a helicopter . The Page should have a fast way to contact us .

We are a mobile AOG team who is available 24/7 . What we do
Scheduled & Unscheduled aircraft maintenance
Major & Minor repairs
STC installations
Aircraft Weight & Balance
Aircraft Painting
Aircraft Cleaning
Maintenance Tracking Utilizing Tracking Programs or spreadsheets
Removal & Installation of Components
Aircraft Pre Buy Inspections
Nice to have
• modern , sleek , aviation

Meet the Staff

Picture with Headset on flying in a helicopter

CEO Mateus Ferreira

Mateus Has been an aircraft mechanic for over 10 years . He has worked for the largest sightseeing & charter tourism company in the New York City area as well as repair stations & manufacturers. He has aircraft specific training to the Kestrane KT420 & Vornel 2K4. He has worked on several airframes including the Belvanko T82 and the Morvell 512. He has held every position in an aircraft maintenance department from mechanic up to Director of Maintenance . His work ethic and ability to manage mechanics in a organized and structured way gives any department or inspection a clear direction .

About Us

TW Aviation Services is company with aircraft maintenance experience . We focus on inspections of aircraft . Our Aircraft Mechanics who are pilots and IA's have experience many aircraft but specialize in the Kestrane KT420 , KT425 , KT435 . The Belvanko T82 and Morvell Tarrant 512 . Our focus is safety and to maintain aircraft day in and day out so our customer can operate the aircraft safely while keeping up with all the manufacturers inspections .

We know aircraft maintenance & maintenance planning . Leave the technical and tedious things to us . Get in your aircraft and fly knowing you have the best maintenance crew in the business.

```html
<!DOCTYPE html>
<html lang="en">
<head>
<meta charset="utf-8">
<title>TW Aviation – Website Design</title>
<link href="https://fonts.googleapis.com/css2?family=Montserrat:wght@400;500&family=Libre+Caslon+Text:wght@400;700&family=Marcellus&family=Lato:wght@400;700&display=swap" rel="stylesheet">
<style>
:root{
  --board-title:#4a6699;
  --brand-blue:#1c6fbf;
  --navy:#1d3f9a;
  --footer-blue:#1f73c1;
  --bar-dark:#2b2b2b;
  --card-line:#e6e6e6;
  --text-dark:#222;
  --white:#fff;
}
*{margin:0;padding:0;box-sizing:border-box}
html,body{width:1200px;height:3158px;overflow:hidden;background:var(--white)}
body{position:relative;font-family:'Lato',sans-serif;color:var(--text-dark)}
.abs{position:absolute}
.board-title{position:absolute;left:0;width:1200px;text-align:center;font-family:'Montserrat',sans-serif;font-weight:400;color:var(--board-title)}
.mockup{position:absolute;left:129px;width:940px;background:var(--white);box-shadow:0 10px 40px rgba(0,0,0,.18)}
/* hero */
.hero{position:absolute;left:25px;top:0;width:890px;height:370px;background:linear-gradient(120deg,#2d8fcf 0%,#4aa3d8 45%,#a9d0ec 70%,#e9f3fa 100%)}
.hero-photo{position:absolute;right:0;top:0;width:560px;height:370px;background:radial-gradient(ellipse at 55% 50%,#c7352a 0 18%,rgba(199,53,42,0) 30%),linear-gradient(160deg,rgba(255,255,255,0) 20%,rgba(240,246,252,.8) 80%)}
.hero-kicker{position:absolute;left:70px;top:77px;font-family:'Libre Caslon Text',serif;font-size:14px;color:var(--white);letter-spacing:.5px;white-space:nowrap}
.hero-title{position:absolute;left:70px;top:100px;font-family:'Marcellus',serif;font-weight:400;font-size:42px;line-height:47px;color:var(--white);letter-spacing:1.5px;white-space:nowrap}
.btn{position:absolute;height:29px;font-size:10px;display:flex;align-items:center;justify-content:center;gap:8px;letter-spacing:.3px}
.btn-book{left:70px;top:277px;width:126px;background:var(--navy);color:var(--white)}
.btn-about{left:211px;top:277px;width:109px;background:var(--white);color:#444}
.section-title{position:absolute;left:0;width:940px;text-align:center;font-family:'Libre Caslon Text',serif;color:var(--brand-blue)}
.insure-card{position:absolute;top:521px;width:214px;height:143px;background:var(--white);box-shadow:0 2px 8px rgba(0,0,0,.12)}
.insure-card .badge{position:absolute;left:50%;top:16px;transform:translateX(-50%)}
.insure-card p{position:absolute;left:47px;right:47px;top:73px;font-family:'Libre Caslon Text',serif;font-size:7px;line-height:9px;color:#777;text-align:center}
.service{position:absolute;width:235px;height:101px;background:var(--white);box-shadow:0 2px 8px rgba(0,0,0,.12);display:flex;align-items:center}
.service svg{margin-left:22px;flex:none}
.service span{margin-left:14px;width:118px;font-size:11.5px;line-height:13px;color:#222}
/* footer */
.footer{position:absolute;background:var(--footer-blue);color:var(--white)}
.footer h4{position:absolute;font-size:14px;font-weight:700;font-family:'Lato',sans-serif;white-space:nowrap}
.footer .small{position:absolute;font-size:8px;line-height:10.5px}
.footer ul{position:absolute;list-style:none;font-size:8px;line-height:16.5px}
.contact-row{position:absolute;display:flex;gap:10px;align-items:flex-start;font-size:8px;line-height:13px;white-space:nowrap}
.contact-row.big{font-size:10px}
.social{position:absolute;display:flex;gap:9px}
.social span{width:23px;height:23px;border-radius:50%;background:var(--white);display:block}
.bar{position:absolute;background:var(--bar-dark);color:#ddd;font-size:8px;display:flex;align-items:center;justify-content:space-between;padding:0 42px}
/* cleaning page */
.nav-logo{position:absolute;left:79px;top:27px;display:flex;align-items:center;gap:5px;font-family:'Libre Caslon Text',serif;font-size:11px;font-weight:700;color:var(--navy);white-space:nowrap}
.nav-logo i{width:16px;height:16px;background:var(--navy);display:block}
.nav-item{position:absolute;top:32px;font-size:9px;color:#555;letter-spacing:.2px;white-space:nowrap}
.nav-item.active{color:var(--brand-blue);font-weight:700}
.nav-phone{position:absolute;left:777px;top:27px;width:80px;height:21px;background:var(--navy);color:var(--white);font-size:8px;display:flex;align-items:center;justify-content:center;border-radius:2px}
.banner{position:absolute;left:107px;top:86px;width:735px;height:301px;background:linear-gradient(180deg,#a9b9c9 0%,#c8cfd6 45%,#b9b9b4 75%,#a8a59c 100%)}
.banner h2{position:absolute;left:0;width:100%;top:122px;text-align:center;font-family:'Marcellus',serif;font-weight:400;font-size:50px;color:#1c3f8f;letter-spacing:1px;white-space:nowrap}
.booking{position:absolute;left:107px;top:404px;width:735px;height:257px;background:var(--white);box-shadow:0 2px 10px rgba(0,0,0,.14)}
.field{position:absolute;border:1.5px solid var(--brand-blue);font-size:10px;color:#333;padding:8px 10px}
.send{position:absolute;left:20px;top:207px;width:83px;height:25px;background:var(--brand-blue);color:var(--white);font-size:9px;display:flex;align-items:center;justify-content:center}
.calendar{position:absolute;left:453px;top:0;width:282px;height:257px;background:var(--footer-blue)}
.cal-head{position:absolute;left:30px;top:16px;width:226px;height:26px;border:1px solid rgba(255,255,255,.8);color:var(--white);font-size:10.5px;font-weight:700;display:flex;align-items:center;justify-content:space-between;padding:0 8px}
.cal-grid{position:absolute;left:30px;top:72px;display:grid;grid-template-columns:repeat(7,26px);column-gap:7.4px;row-gap:7px}
.cal-grid span{height:26px;border:1px solid rgba(255,255,255,.7);color:var(--white);font-size:7px;display:flex;align-items:center;justify-content:center}
.cal-grid .sel{background:#153a78;border-color:#153a78;font-weight:700}
.cal-grid .next{background:var(--white);color:var(--brand-blue)}
</style>
</head>
<body>

<h1 class="board-title" style="top:120px;font-size:62px;">home page</h1>

<section class="mockup home" style="top:236px;height:1411px;">
  <div class="hero" role="img" aria-label="Red helicopter flying against a blue sky with white clouds">
    <div class="hero-photo"></div>
    <p class="hero-kicker">WELCOME TO AIRCRAFT CLEANING</p>
    <h2 class="hero-title">Best Aviation<br>Maintenance<br>Provider</h2>
    <a class="btn btn-book">BOOK ONLINE <svg width="18" height="8" viewBox="0 0 18 8"><path d="M0 4h16M12 1l4 3-4 3" stroke="#fff" fill="none" stroke-width="1.2"/></svg></a>
    <a class="btn btn-about">ABOUT US <svg width="14" height="8" viewBox="0 0 14 8"><path d="M0 4h12M9 1l3 3-3 3" stroke="#444" fill="none" stroke-width="1.2"/></svg></a>
  </div>

  <h3 class="section-title" style="top:424px;font-size:26px;">TW AVIATION INSURED</h3>

  <div class="insure-card" style="left:127px;">
    <svg class="badge" width="40" height="40"><rect x="4" y="8" width="32" height="24" rx="3" fill="#2aa7c9"/></svg>
    <p>Lorem Ipsum is simply dummy text of the printing and typesetting industry.</p>
  </div>
  <div class="insure-card" style="left:367px;">
    <svg class="badge" width="44" height="44"><circle cx="22" cy="22" r="21" fill="#c9a23a"/><circle cx="22" cy="22" r="15" fill="#1d3f9a"/></svg>
    <p>Lorem Ipsum is simply dummy text of the printing and typesetting industry.</p>
  </div>
  <div class="insure-card" style="left:606px;">
    <svg class="badge" width="50" height="34"><rect x="3" y="6" width="44" height="22" rx="2" fill="#2a3591"/></svg>
    <p>Lorem Ipsum is simply dummy text of the printing and typesetting industry.</p>
  </div>

  <h3 class="section-title" style="top:740px;font-size:28px;font-weight:700;">WHAT WE DO</h3>

  <div class="service" style="left:88px;top:796px;"><svg width="58" height="58" viewBox="0 0 58 58" fill="none" stroke="#1c6fbf" stroke-width="1.6"><path d="M4 44c8-6 16-6 24-2h14c3 0 3 4 0 4H30M4 52l10-6h18l16-10c3-2 6 1 3 4L36 54H4"/><path d="M26 6v24M22 6h8M38 6c-3 0-5 2-5 5s2 5 5 5 5-2 5-5M38 16v14"/></svg><span>Major &amp; Minor repairs</span></div>
  <div class="service" style="left:352px;top:796px;"><svg width="58" height="58" viewBox="0 0 58 58" fill="none" stroke="#1c6fbf" stroke-width="1.6"><rect x="4" y="12" width="40" height="28" rx="2"/><path d="M18 48h12M24 40v8M14 52h20"/><circle cx="42" cy="14" r="8"/><circle cx="42" cy="14" r="3"/><circle cx="22" cy="26" r="6"/></svg><span>STC installations</span></div>
  <div class="service" style="left:617px;top:796px;"><svg width="58" height="58" viewBox="0 0 58 58" fill="none" stroke="#1c6fbf" stroke-width="1.6"><path d="M36 4v30M24 10h24M24 10l-5 12h10zM48 10l-5 12h10zM30 34h12"/><path d="M4 42c8-6 16-6 24-2h10c3 0 3 4 0 4H28M4 52l10-6h16l14-9c3-2 6 1 3 4L32 54H4"/></svg><span>Aircraft Weight &amp;<br>Balance</span></div>

  <div class="service" style="left:88px;top:917px;"><svg width="58" height="58" viewBox="0 0 58 58" fill="none" stroke="#1c6fbf" stroke-width="1.6"><path d="M28 6h10v14H28zM14 24h36v10H14zM30 34l-4 18h10l-2-18M6 29h8M4 22l6 3M4 36l6-3"/></svg><span>Aircraft Painting</span></div>
  <div class="service" style="left:352px;top:917px;"><svg width="58" height="58" viewBox="0 0 58 58" fill="none" stroke="#1c6fbf" stroke-width="1.6"><rect x="10" y="18" width="36" height="20" rx="2"/><circle cx="28" cy="28" r="5"/><circle cx="12" cy="8" r="5"/><circle cx="44" cy="8" r="5"/><path d="M17 8h22M10 48h36M28 38v10M8 52h10"/></svg><span>Aircraft Cleaning</span></div>
  <div class="service" style="left:617px;top:917px;"><svg width="58" height="58" viewBox="0 0 58 58" fill="none" stroke="#1c6fbf" stroke-width="1.6"><path d="M14 26C6 16 6 6 14 4s12 6 8 12z"/><circle cx="14" cy="12" r="3"/><path d="M14 26c0 6 4 10 10 10h8c6 0 6 10 0 10H14"/><circle cx="48" cy="44" r="6"/></svg><span>Maintenance Tracking<br>Utilizing Tracking<br>Programs or<br>spreadsheets</span></div>

  <div class="service" style="left:88px;top:1039px;"><svg width="58" height="58" viewBox="0 0 58 58" fill="none" stroke="#1c6fbf" stroke-width="1.6"><rect x="4" y="8" width="46" height="40" rx="2"/><path d="M4 18h46M14 4v8M40 4v8M4 28h46M4 38h46M16 18v30M28 18v30M40 18v30"/><circle cx="46" cy="48" r="8" fill="#fff"/><path d="M42 48l3 3 5-6"/></svg><span>Scheduled &amp;<br>Unscheduled aircraft<br>maintenance</span></div>
  <div class="service" style="left:352px;top:1039px;"><svg width="58" height="58" viewBox="0 0 58 58" fill="none" stroke="#1c6fbf" stroke-width="1.6"><rect x="12" y="30" width="26" height="16" rx="2"/><circle cx="8" cy="48" r="5"/><path d="M20 30V18h10v12M34 10l6-6M40 10l8 8M46 30v20M40 50h14M4 40h8"/></svg><span>Removal &amp;<br>Installation of<br>Components</span></div>
  <div class="service" style="left:617px;top:1039px;"><svg width="58" height="58" viewBox="0 0 58 58" fill="none" stroke="#1c6fbf" stroke-width="1.6"><path d="M18 4h26v46H18zM24 14h14M24 22h14M24 30h14M24 38h8"/><path d="M10 14v20M14 18c-2-2-8-2-8 2s8 4 8 8-6 4-8 2"/><rect x="4" y="40" width="12" height="4"/><rect x="4" y="46" width="12" height="4"/><circle cx="44" cy="44" r="7"/></svg><span>Aircraft Pre Buy<br>Inspections</span></div>

  <footer class="footer" style="left:25px;top:1166px;width:890px;height:212px;">
    <h4 style="left:93px;top:42px;">About Us</h4>
    <p class="small" style="left:93px;top:74px;width:142px;">Lorem Ipsum is simply dummy text of the printing and typesetting industry. Lorem Ipsum has been the industry's standard dummy text ever since the 1500s.</p>
    <h4 style="left:293px;top:40px;">Quick Links</h4>
    <ul style="left:293px;top:68px;"><li>Home page</li><li>Aircraft Maintenance</li><li>Aircraft Cleaning</li><li>About Us</li><li>Contact</li><li>Careers</li></ul>
    <h4 style="left:451px;top:40px;">Contact us</h4>
    <div class="contact-row" style="left:451px;top:72px;"><svg width="13" height="11"><rect x="1" y="1" width="11" height="9" fill="none" stroke="#fff"/><path d="M1 1l5.5 5L12 1" fill="none" stroke="#fff"/></svg>dana.hollis@example.com</div>
    <div class="contact-row big" style="left:451px;top:100px;"><svg width="11" height="14"><path d="M5.5 13C2 8 1 6 1 5a4.5 4.5 0 0 1 9 0c0 1-1 3-4.5 8z" fill="none" stroke="#fff"/><circle cx="5.5" cy="5" r="1.6" fill="none" stroke="#fff"/></svg>Lorem ipsum dolor sit amet,<br>consectetur adipiscing elit.</div>
    <h4 style="left:679px;top:40px;">Follow us</h4>
    <div class="social" style="left:679px;top:72px;"><span></span><span></span><span></span><span></span></div>
  </footer>
  <div class="bar" style="left:25px;top:1378px;width:890px;height:29px;"><span>©2020 HARBOR PLUMBING, All Right Reserved</span><span>Terms &amp; Condition | Privacy Policy</span></div>
</section>

<h1 class="board-title" style="top:1860px;font-size:64px;">Aircraft Cleaning</h1>

<section class="mockup cleaning" style="top:2030px;height:952px;">
  <div class="abs" style="left:0;top:68px;width:940px;height:3px;background:#d9d9d9;"></div>
  <div class="nav-logo"><i></i>TW Aviation</div>
  <span class="nav-item" style="left:198px;">HOME PAGE</span>
  <span class="nav-item" style="left:279px;">AIRCRAFT MAINTENANCE</span>
  <span class="nav-item active" style="left:417px;">AIRCRAFT CLEANING</span>
  <span class="nav-item" style="left:535px;">ABOUT US</span>
  <span class="nav-item" style="left:607px;">CONTACT</span>
  <span class="nav-item" style="left:677px;">CAREERS</span>
  <span class="nav-phone">0800-555-014</span>

  <div class="banner" role="img" aria-label="Crew in hi-vis vests cleaning a private jet on the apron by a hangar">
    <h2>Book Our Servies Now</h2>
  </div>

  <div class="booking">
    <div class="field" style="left:20px;top:20px;width:200px;height:32px;">Name</div>
    <div class="field" style="left:229px;top:20px;width:200px;height:32px;">Email</div>
    <div class="field" style="left:20px;top:67px;width:409px;height:31px;">Subject</div>
    <div class="field" style="left:20px;top:110px;width:409px;height:80px;">Message</div>
    <div class="send">Send</div>
    <div class="calendar">
      <div class="cal-head">December 2020 <svg width="7" height="10"><path d="M1 1l4 4-4 4" stroke="#fff" fill="none" stroke-width="1.4"/></svg></div>
      <div class="cal-grid">
        <span>1</span><span>2</span><span>3</span><span>4</span><span>5</span><span>6</span><span>7</span>
        <span>8</span><span>9</span><span>10</span><span>11</span><span>12</span><span>13</span><span>14</span>
        <span>15</span><span>16</span><span>17</span><span>18</span><span>19</span><span>20</span><span>21</span>
        <span>22</span><span>23</span><span>24</span><span>25</span><span>26</span><span>27</span><span>28</span>
        <span>29</span><span class="sel">30</span><span class="next">1</span><span class="next">2</span><span class="next">3</span><span class="next">4</span><span class="next">5</span>
      </div>
    </div>
  </div>

  <footer class="footer" style="left:0;top:683px;width:940px;height:230px;">
    <h4 style="left:97px;top:53px;">About Us</h4>
    <p class="small" style="left:97px;top:86px;width:145px;">Lorem Ipsum is simply dummy text of the printing and typesetting industry. Lorem Ipsum has been the industry's standard dummy text ever since the 1500s.</p>
    <h4 style="left:309px;top:51px;">Quick Links</h4>
    <ul style="left:309px;top:80px;line-height:18px;"><li>Home page</li><li>Aircraft Maintenance</li><li>Aircraft Cleaning</li><li>About Us</li><li>Contact</li><li>Careers</li></ul>
    <h4 style="left:475px;top:51px;">Contact us</h4>
    <div class="contact-row" style="left:475px;top:84px;"><svg width="13" height="11"><rect x="1" y="1" width="11" height="9" fill="none" stroke="#fff"/><path d="M1 1l5.5 5L12 1" fill="none" stroke="#fff"/></svg>dana.hollis@example.com</div>
    <div class="contact-row big" style="left:475px;top:118px;"><svg width="11" height="14"><path d="M5.5 13C2 8 1 6 1 5a4.5 4.5 0 0 1 9 0c0 1-1 3-4.5 8z" fill="none" stroke="#fff"/><circle cx="5.5" cy="5" r="1.6" fill="none" stroke="#fff"/></svg>Lorem ipsum dolor sit amet,<br>consectetur adipiscing elit.</div>
    <h4 style="left:715px;top:51px;">Follow us</h4>
    <div class="social" style="left:715px;top:85px;"><span></span><span></span><span></span><span></span></div>
  </footer>
  <div class="bar" style="left:0;top:913px;width:940px;height:33px;"><span>©2020 HARBOR PLUMBING, All Right Reserved</span><span>Terms &amp; Condition | Privacy Policy</span></div>
</section>

</body>
</html>
```